Bookcover: Lessons From the Silent Orchard

I am publishing a super-low-cost innovation book for €4,99 on Bravolo Self Release to help everyone become a great innovator: young ambitious people without college education nor a big budget. Do you want to help me?

Brief:
Design a book cover 1600 x 2560 pixels for BSR.
Main title: Lessons From the Silent Orchard
Sub title: mindset - insights - skills & tools
Author: Maarten de Klerk
Design: captive, and appealing to everyone
Target Group: young ambitious people without college education

For bravolo please format the height/width ratio of 1.6:1

```html
<!DOCTYPE html>
<html lang="en">
<head>
<meta charset="utf-8">
<title>Lessons From the Silent Orchard — Book Cover</title>
<link href="https://fonts.googleapis.com/css2?family=Bebas+Neue&family=Montserrat:wght@400;600&display=swap" rel="stylesheet">
<style>
  :root {
    --backdrop: #000000;
    --cover-cream: #EDDBC2;
    --title-orange: #F39322;
    --title-blue: #0F69AA;
    --ink-dark: #2A2325;
    --rule-orange: #F0A040;
    --art-gold: #F0B233;
    --art-gold-deep: #E79A2A;
  }
  html, body {
    margin: 0;
    padding: 0;
    width: 1200px;
    height: 1200px;
    overflow: hidden;
    background: var(--backdrop);
  }
  .book-cover {
    position: absolute;
    left: 240px;
    top: 24px;
    width: 720px;
    height: 1152px;
    background: var(--cover-cream);
  }
  .book-cover svg {
    display: block;
    width: 720px;
    height: 1152px;
  }
  .title-line {
    font-family: "Bebas Neue", "Oswald", sans-serif;
  }
  .title-orange { fill: var(--title-orange); }
  .title-blue { fill: var(--title-blue); }
  .title-rule { fill: var(--title-orange); }
  .subtitle {
    font-family: "Montserrat", "Helvetica Neue", sans-serif;
    font-weight: 400;
    font-size: 27px;
    fill: var(--ink-dark);
    letter-spacing: 0.5px;
  }
  .subtitle-rule {
    stroke: var(--rule-orange);
    stroke-width: 1.2;
  }
  .author-name {
    font-family: "Montserrat", "Helvetica Neue", sans-serif;
    font-weight: 600;
    font-size: 57px;
    fill: var(--ink-dark);
  }
</style>
</head>
<body>
  <div class="book-cover">
    <svg viewBox="0 0 720 1152" xmlns="http://www.w3.org/2000/svg">
      <defs>
        <radialGradient id="art-glow" cx="50%" cy="45%" r="60%">
          <stop offset="0%" stop-color="#F6C04A"/>
          <stop offset="70%" stop-color="#F0B233"/>
          <stop offset="100%" stop-color="#EDDBC2" stop-opacity="0"/>
        </radialGradient>
      </defs>

      <!-- Title block -->
      <rect class="title-rule" x="82" y="91" width="140" height="9"/>
      <rect class="title-rule" x="498" y="91" width="140" height="9"/>
      <text class="title-line title-orange" x="360" y="100" font-size="97" text-anchor="middle" textLength="262" lengthAdjust="spacingAndGlyphs">LESSONS</text>

      <text class="title-line title-orange" x="82" y="251" font-size="186" textLength="556" lengthAdjust="spacingAndGlyphs">FROM THE</text>
      <text class="title-line title-blue" x="82" y="482" font-size="313" textLength="556" lengthAdjust="spacingAndGlyphs">SILENT</text>
      <text class="title-line title-blue" x="82" y="616" font-size="171" textLength="556" lengthAdjust="spacingAndGlyphs">ORCHARD</text>

      <!-- Subtitle -->
      <line class="subtitle-rule" x1="128" y1="648" x2="592" y2="648"/>
      <text class="subtitle" x="360" y="675" text-anchor="middle">mindset - insights - skills &amp; tools</text>
      <line class="subtitle-rule" x1="128" y1="688" x2="592" y2="688"/>

      <!-- Cover illustration area -->
      <g role="img" aria-label="Illustration: a person rising out of an opened yellow light bulb, holding up a sparkling diamond, with small clouds around">
        <ellipse cx="370" cy="860" rx="160" ry="150" fill="url(#art-glow)"/>
      </g>

      <!-- Author -->
      <text class="author-name" x="368" y="1104" text-anchor="middle">Maarten de Klerk</text>
    </svg>
  </div>
</body>
</html>
```